Brave Tindle website (tool sales website)

place to sell tools that are used to install tiles. We have over 100 tools that can be divided into 5-6 categories we plan to sell our tools online

The business purchases tools wholesale and sells them to customers retail via social media and soon by online website

The product consists of tools and the blades that are used mostly to cut and install tiles like floor tile, shower tiles

Target Market(s)

The target market includes individuals in the building trade and those learning the trade. For example trade schools have used this business exclusively for the tools they need.

Industry/Entity Type

Sales

Coding

Coded - Design and coding required

Number of Pages Required

1 page

Requirements
Must have
• Color and imagery complimentary to the attached logo
• We have approximately 100 items for sale now and think a home page and 5 pages with different tool categories might work best. Categories would be Dimond blade cutting; Coring and Drilling; Grinding and polishing; Manual tile cutters; Other.
• Really only need the space on each page to put the items. We can use Dreamweaver to place actual items and finish the site.
Nice to have
• Need to incorporate a cart for purchases
• We envision something like the US retailer Marlowbee's website, just not as complex. Home page with general info and 5 areas to go to 5 pages each with multiple spots for tools to be listed with info. There is a screen shot below as an example of one of the five
• pages

```html
<!DOCTYPE html>
<html lang="en">
<head>
<meta charset="utf-8">
<title>Brave Tindle Diamond Blades</title>
<link href="https://fonts.googleapis.com/css2?family=Roboto:wght@400;500;700&display=swap" rel="stylesheet">
<style>
:root{
  --red:#c8102e;
  --red-dark:#b00d25;
  --ink:#222;
  --text:#555;
  --muted:#777;
  --line:#e2e2e2;
  --soft:#f4f5f7;
  --footer:#2b2b2b;
  --white:#fff;
}
*{box-sizing:border-box;margin:0;padding:0}
html,body{width:1200px;height:2639px;overflow:hidden}
body{position:relative;background:var(--white);font-family:'Roboto',Arial,sans-serif;color:var(--ink)}
.abs{position:absolute}

.top-rule{left:0;top:0;width:1200px;height:5px;background:var(--red)}
.header{left:0;top:5px;width:1200px;height:183px;background:linear-gradient(#fff,#f7f7f7);border-bottom:1px solid var(--line)}
.brand{left:86px;top:50px;width:180px;text-align:center}
.brand-mark{width:40px;height:40px;border-radius:50%;background:var(--red);margin:0 auto 10px}
.brand-name{font-size:19px;font-weight:700;line-height:22px;color:var(--ink)}
.nav a{position:absolute;top:53px;font-size:12px;color:var(--ink);text-decoration:none;letter-spacing:.3px}
.nav a.active{color:var(--red)}
.search{left:290px;top:123px;width:347px;height:44px;border:1px solid var(--line);background:#fff}
.search svg{position:absolute;left:16px;top:14px}
.search .ph{position:absolute;left:62px;top:14px;font-size:12px;color:var(--muted)}
.search .btn{position:absolute;right:-1px;top:-1px;width:81px;height:44px;background:var(--red);color:#fff;font-size:13px;font-weight:500;text-align:center;line-height:44px}
.util{top:124px;font-size:13px;line-height:19px;color:var(--ink)}
.util b{display:block;font-weight:400;color:var(--red)}
.util-sep{top:124px;width:1px;height:40px;background:var(--line)}
.caret{display:inline-block;border:4px solid transparent;border-top:5px solid var(--muted);vertical-align:-3px;margin-left:6px}

.perks{left:0;top:188px;width:1200px;height:67px}
.perk{top:20px;width:300px;text-align:center}
.perk h4{font-size:13px;font-weight:500;letter-spacing:.3px}
.perk p{font-size:11px;color:var(--muted);margin-top:5px}
.perk-sep{top:12px;width:1px;height:44px;background:var(--line)}

.hero{left:86px;top:273px;width:1028px;height:426px;background:radial-gradient(circle at 32% 45%,#8a6a45 0%,#3b2a1b 35%,#141010 70%)}
.hero h1{position:absolute;left:672px;top:182px;font-size:42px;font-weight:500;color:#fff;letter-spacing:1px}
.hero p{position:absolute;left:675px;top:244px;width:330px;font-size:11px;line-height:22px;color:#eee}
.dots{left:491px;top:676px}
.dots i{display:inline-block;width:10px;height:10px;border-radius:50%;background:#fff;margin:0 3px}
.dots i.on{background:var(--red)}

.cat{overflow:hidden}
.cat-label{position:absolute;left:50%;bottom:28px;transform:translateX(-50%);width:255px;height:50px;line-height:50px;text-align:center;background:rgba(235,235,235,.72);font-size:16px;color:#333;letter-spacing:.3px}
.cat-feature{left:435px;top:1131px;width:331px;height:150px;background:var(--red);color:#fff;text-align:center;padding:26px 28px 0}
.cat-feature h3{font-size:16px;font-weight:500}
.cat-feature p{font-size:11px;line-height:21px;margin-top:10px}

.products{left:0;top:1320px;width:1200px;height:515px;background:var(--soft)}
.section-title{width:1200px;text-align:center;font-size:20px;font-weight:500;color:var(--red);letter-spacing:.5px}
.tabs{left:0;top:1398px;width:1200px;text-align:center;font-size:11px;color:var(--text)}
.tabs span{margin:0 28px}
.card{top:1440px;width:243px;height:355px;background:#fff;border:1px solid #ececec}
.card .thumb{position:absolute;left:7px;top:9px;width:229px;height:206px;border:1px solid #e6e6e6}
.card .price{position:absolute;top:232px;width:100%;text-align:center;font-size:21px;font-weight:700;color:var(--red)}
.card .name{position:absolute;top:272px;width:100%;text-align:center;font-size:14px;color:#333}
.card .acts{position:absolute;top:307px;width:100%;text-align:center}
.card .acts span{display:inline-block;width:33px;height:33px;border:1px solid #ccc;border-radius:50%;margin:0 3px;line-height:33px}
.card .acts svg{vertical-align:middle}

.quote{left:176px;top:1916px;width:537px;font-size:11.5px;line-height:22px;color:var(--text)}
.qmark{font-size:34px;color:#ccc;font-family:Georgia,serif}
.author{left:178px;top:2038px;font-size:14px;font-weight:700;color:var(--red)}
.author-date{left:178px;top:2060px;font-size:11px;color:var(--muted)}
.portrait{left:776px;top:1888px;width:194px;height:194px;border-radius:50%;border:4px solid #eee;background:radial-gradient(circle at 50% 40%,#d9a98a,#8b5a3c 60%,#c9c3bd)}

.newsletter{left:0;top:2129px;width:1200px;height:285px;background:var(--soft)}
.newsletter p{position:absolute;left:240px;top:98px;width:720px;text-align:center;font-size:11.5px;line-height:22px;color:var(--text)}
.sub-form{left:285px;top:2305px;width:630px;height:53px;background:#fff;border:1px solid #ddd}
.sub-form .ph{position:absolute;left:16px;top:18px;font-size:12px;color:var(--muted)}
.sub-form .btn{position:absolute;right:-1px;top:-1px;width:149px;height:53px;background:var(--red);color:#fff;font-size:14px;font-weight:500;text-align:center;line-height:53px}

.footer{left:0;top:2414px;width:1200px;height:225px;background:var(--footer)}
.social{top:2448px;width:60px;height:60px;border:1px solid #777;border-radius:50%}
.social svg{position:absolute;left:19px;top:21px}
.footer-rule{left:86px;top:2522px;width:1028px;height:1px;background:#3d3d3d}
.footer-links{left:0;top:2546px;width:1200px;text-align:center;font-size:11.5px;color:#ddd}
.footer-links span{margin:0 24px}
.footer-links i{font-style:normal;color:#888}
.copy{left:0;top:2590px;width:1200px;text-align:center;font-size:11.5px;color:#ddd}
</style>
</head>
<body>

<div class="abs top-rule"></div>
<header class="abs header">
  <div class="abs brand" style="top:16px">
    <div class="brand-mark"></div>
    <div class="brand-name">Brave Tindle's<br>Diamond Blades</div>
  </div>
  <nav class="nav">
    <a class="active" style="left:607px">HOME</a>
    <a style="left:699px">ABOUT US</a>
    <a style="left:811px">SERVICES</a>
    <a style="left:922px">PRODUCTS</a>
    <a style="left:1040px">CONTACT US</a>
  </nav>
</header>
<div class="abs search">
  <svg width="16" height="16" viewBox="0 0 16 16"><circle cx="6.5" cy="6.5" r="5" fill="none" stroke="#666" stroke-width="1.6"/><line x1="10.5" y1="10.5" x2="14.5" y2="14.5" stroke="#666" stroke-width="1.6"/></svg>
  <span class="ph">Enter Any keyword here</span>
  <span class="btn">SEARCH</span>
</div>
<div class="abs util-sep" style="left:664px"></div>
<div class="abs util" style="left:681px">Shop by<b>Category<i class="caret"></i></b></div>
<div class="abs util-sep" style="left:782px"></div>
<div class="abs util" style="left:799px">Hello. Sign in<b>Your Account<i class="caret" style="margin-left:14px"></i></b></div>
<div class="abs util-sep" style="left:940px"></div>
<div class="abs util" style="left:955px">Wish<b>List<i class="caret"></i></b></div>
<div class="abs util-sep" style="left:1013px"></div>
<svg class="abs" style="left:1030px;top:126px" width="32" height="30" viewBox="0 0 32 30"><path d="M2 4h5l4 15h15l3-10H9" fill="none" stroke="#333" stroke-width="1.6"/><circle cx="13" cy="24" r="2" fill="#333"/><circle cx="24" cy="24" r="2" fill="#333"/><text x="16" y="10" font-size="10" fill="#c8102e" font-family="Roboto,sans-serif">0</text></svg>
<div class="abs util" style="left:1071px;top:144px">Cart<i class="caret"></i></div>

<section class="abs perks">
  <div class="abs perk" style="left:142px"><h4>FREE DELIVERY WORLDWIDE</h4><p>Click here for more info</p></div>
  <div class="abs perk-sep" style="left:472px"></div>
  <div class="abs perk" style="left:464px"><h4>FINAL CLEARANCE SALE</h4><p>Up to 70% off</p></div>
  <div class="abs perk-sep" style="left:774px"></div>
  <div class="abs perk" style="left:776px"><h4>NORTHFIELD A-LIST</h4><p>Earn point while you shop!</p></div>
</section>

<section class="abs hero" role="img" aria-label="Angle grinder cutting metal with a shower of sparks">
  <h1>BRAVE TINDLE</h1>
  <p>Sed ut perspiciatis unde omnis iste natus error sit voluptatem accusantium doloremque laudantium, totam rem aperiam, eaque beatae vitae dicta sunt explicabo.</p>
</section>
<div class="abs dots"><i></i><i class="on"></i><i></i></div>

<div class="abs cat" style="left:86px;top:727px;width:331px;height:269px;background:linear-gradient(135deg,#9a8877,#6e6058)" role="img" aria-label="Core drill on a rubble-covered floor">
  <div class="cat-label">CORING &amp; DRILLING</div>
</div>
<div class="abs cat" style="left:435px;top:727px;width:331px;height:404px;background:radial-gradient(circle at 45% 70%,#c88a3e,#4e4640 45%,#2c2a2a)" role="img" aria-label="Chop saw cutting a steel bar with sparks"></div>
<div class="abs cat-feature">
  <h3>DIAMOND BLADE CUTTING</h3>
  <p>Sed ut perspiciatis unde omnis iste natus error sit voluptatem accusantium doloremque laudantium, totam architecto beatae vitae dicta sunt explicabo.</p>
</div>
<div class="abs cat" style="left:781px;top:727px;width:331px;height:269px;background:linear-gradient(135deg,#b7aa98,#d8d0c4)" role="img" aria-label="Manual tile cutter scoring a floor tile">
  <div class="cat-label">MANUAL TILE CUTTERS</div>
</div>
<div class="abs cat" style="left:86px;top:1012px;width:331px;height:269px;background:linear-gradient(135deg,#3a3d44,#6b6e75)" role="img" aria-label="Gloved hands grinding and polishing metal">
  <div class="cat-label">GRINDING &amp; POLISHING</div>
</div>
<div class="abs cat" style="left:781px;top:1012px;width:331px;height:269px;background:linear-gradient(135deg,#5c5b5a,#9b9590)" role="img" aria-label="Angle grinder with flap disc and spare blades">
  <div class="cat-label">OTHER</div>
</div>

<section class="abs products"></section>
<h2 class="abs section-title" style="left:0;top:1350px">OUR PRODUCTS</h2>
<div class="abs tabs"><span>NEW ARRIVALS</span><i style="font-style:normal">|</i><span>BEST SELLERS</span></div>

<div class="abs card" style="left:79px">
  <div class="thumb" role="img" aria-label="Diamond saw blades" style="background:radial-gradient(circle,#d6d6d6,#f1f1f1 70%)"></div>
  <div class="price">$250.00</div><div class="name">CONTRARY TO POPULAR</div>
  <div class="acts"><span><svg width="12" height="12" viewBox="0 0 12 12"><path d="M1 2h2l2 6h5l1-4H4" fill="none" stroke="#666"/></svg></span><span><svg width="12" height="12" viewBox="0 0 12 12"><path d="M6 10 2 6a2 2 0 0 1 4-3 2 2 0 0 1 4 3z" fill="none" stroke="#666"/></svg></span><span><svg width="12" height="12" viewBox="0 0 12 12"><path d="M1 4h9l-2-2M11 8H2l2 2" fill="none" stroke="#666"/></svg></span></div>
</div>
<div class="abs card" style="left:338px">
  <div class="thumb" role="img" aria-label="Yellow rotary hammer drill" style="background:radial-gradient(circle,#e9dfa5,#f3f3f3 65%)"></div>
  <div class="price">$250.00</div><div class="name">CONTRARY TO POPULAR</div>
  <div class="acts"><span><svg width="12" height="12" viewBox="0 0 12 12"><path d="M1 2h2l2 6h5l1-4H4" fill="none" stroke="#666"/></svg></span><span><svg width="12" height="12" viewBox="0 0 12 12"><path d="M6 10 2 6a2 2 0 0 1 4-3 2 2 0 0 1 4 3z" fill="none" stroke="#666"/></svg></span><span><svg width="12" height="12" viewBox="0 0 12 12"><path d="M1 4h9l-2-2M11 8H2l2 2" fill="none" stroke="#666"/></svg></span></div>
</div>
<div class="abs card" style="left:598px">
  <div class="thumb" role="img" aria-label="Manual tile cutter with red handle" style="background:radial-gradient(circle,#dcd2d2,#f3f3f3 65%)"></div>
  <div class="price">$250.00</div><div class="name">CONTRARY TO POPULAR</div>
  <div class="acts"><span><svg width="12" height="12" viewBox="0 0 12 12"><path d="M1 2h2l2 6h5l1-4H4" fill="none" stroke="#666"/></svg></span><span><svg width="12" height="12" viewBox="0 0 12 12"><path d="M6 10 2 6a2 2 0 0 1 4-3 2 2 0 0 1 4 3z" fill="none" stroke="#666"/></svg></span><span><svg width="12" height="12" viewBox="0 0 12 12"><path d="M1 4h9l-2-2M11 8H2l2 2" fill="none" stroke="#666"/></svg></span></div>
</div>
<div class="abs card" style="left:859px">
  <div class="thumb" role="img" aria-label="Diamond cup grinding wheels" style="background:radial-gradient(circle,#cfc6b8,#f3f3f3 65%)"></div>
  <div class="price">$250.00</div><div class="name">CONTRARY TO POPULAR</div>
  <div class="acts"><span><svg width="12" height="12" viewBox="0 0 12 12"><path d="M1 2h2l2 6h5l1-4H4" fill="none" stroke="#666"/></svg></span><span><svg width="12" height="12" viewBox="0 0 12 12"><path d="M6 10 2 6a2 2 0 0 1 4-3 2 2 0 0 1 4 3z" fill="none" stroke="#666"/></svg></span><span><svg width="12" height="12" viewBox="0 0 12 12"><path d="M1 4h9l-2-2M11 8H2l2 2" fill="none" stroke="#666"/></svg></span></div>
</div>

<div class="abs qmark" style="left:156px;top:1880px">&ldquo;</div>
<p class="abs quote">Sed ut perspiciatis unde omnis iste natus error sit voluptatem accusantium doloremque laudantium, totam rem aperiam, eaque ipsa quae ab illo inventore veritatis et quasi architecto beatae vitae dicta sunt explicabo. Nemo enim ipsam voluptatem quia voluptas sit aspernatur aut odit aut fugit, sed quia consequuntur magni dolores eos qui ratione voluptatem sequi nesciunt.</p>
<div class="abs qmark" style="left:560px;top:1998px">&rdquo;</div>
<div class="abs author">DARA VELLING</div>
<div class="abs author-date">posed on 25 June 2017</div>
<div class="abs portrait" role="img" aria-label="Portrait of a smiling customer"></div>

<section class="abs newsletter">
  <h2 class="abs section-title" style="left:0;top:50px">SUBSCRIBE TO OUR NEWSLETTER</h2>
  <p>Sed ut perspiciatis unde omnis iste natus error sit voluptatem accusantium doloremque laudantium, totam rem aperiam, eaque ipsa quae ab illo inventore veritatis et quasi architecto beatae vitae dicta sunt explicabo.</p>
</section>
<div class="abs sub-form"><span class="ph">Enter Your Email id :</span><span class="btn">SUBSCRIBE</span></div>

<footer class="abs footer"></footer>
<div class="abs social" style="left:389px"></div>
<div class="abs social" style="left:461px"></div>
<div class="abs social" style="left:531px"></div>
<div class="abs social" style="left:604px"></div>
<div class="abs social" style="left:674px"></div>
<div class="abs social" style="left:746px"><svg width="20" height="16" viewBox="0 0 20 16"><rect x="1" y="1" width="18" height="14" fill="none" stroke="#fff" stroke-width="1.5"/><path d="M1 1l9 8 9-8" fill="none" stroke="#fff" stroke-width="1.5"/></svg></div>
<div class="abs footer-rule"></div>
<div class="abs footer-links"><span>HOME</span><i>|</i><span>ABOUT US</span><i>|</i><span>SERVICES</span><i>|</i><span>PRODUCTS</span><i>|</i><span>CONTACT US</span></div>
<div class="abs copy">&copy; Copyrights 2017 Brave Tindle All Rights Reserved.</div>

</body>
</html>
```